label design for soy candle

I am a start up making soy candles and other products involving scents.
On the label should be in writing : the scent, Handgemacht in der Schweiz, Sojakerze, my logo with the name Pertwick Candles on it. I will upload the currant label of my candles, but I want something more fashioned. The color of the label should be black with the scent written in gold, and the rest in white. Or maybe suggest something different, I am open to new designs. I am also open to change the logo, except the flower has to stay.
Sizes : square 60x60mm / round 50mm / rectangle 70x20mm ( for different jars )

```html
<!DOCTYPE html>
<html lang="de">
<head>
<meta charset="utf-8">
<title>Pertwick Candles – Sojakerze Etikett</title>
<link href="https://fonts.googleapis.com/css2?family=Poiret+One&family=Josefin+Sans:wght@300&family=Kaushan+Script&display=swap" rel="stylesheet">
<style>
  :root {
    --label-black: #0f0f0f;
    --cream: #f3e6b4;
    --pale-gold: #e6d6a0;
    --scent-gold: #d3a92e;
  }
  html, body {
    margin: 0;
    padding: 0;
    overflow: hidden;
    background: var(--label-black);
  }
  .label {
    position: relative;
    width: 1200px;
    height: 343px;
    background: var(--label-black);
    overflow: hidden;
  }
  .flower-mark {
    position: absolute;
    left: 556px;
    top: 18px;
    width: 80px;
    height: 80px;
    border-radius: 50%;
    background: var(--cream);
  }
  .divider {
    position: absolute;
    left: 414px;
    top: 127px;
    width: 358px;
    height: 3px;
    background: var(--cream);
  }
  .brand-name {
    position: absolute;
    left: 0;
    width: 1200px;
    top: 134px;
    margin: 0;
    text-align: center;
    font-family: "Poiret One", sans-serif;
    font-weight: 400;
    font-size: 100px;
    line-height: 1;
    color: var(--cream);
    white-space: nowrap;
    transform: scaleX(0.68);
    transform-origin: 600px 0;
  }
  .scent-name {
    position: absolute;
    left: 0;
    width: 1200px;
    top: 226px;
    margin: 0;
    text-align: center;
    font-family: "Kaushan Script", cursive;
    font-weight: 400;
    font-size: 70px;
    line-height: 1.1;
    color: var(--scent-gold);
  }
  .product-type,
  .origin {
    position: absolute;
    margin: 0;
    font-family: "Josefin Sans", sans-serif;
    font-weight: 300;
    color: var(--pale-gold);
    text-align: center;
    white-space: nowrap;
  }
  .product-type {
    left: 145px;
    top: 179px;
    font-size: 17px;
    letter-spacing: 1.5px;
    line-height: 1;
  }
  .origin {
    left: 945px;
    width: 200px;
    top: 175px;
    font-size: 18px;
    letter-spacing: 2px;
    line-height: 27px;
  }
</style>
</head>
<body>
  <main class="label">
    <div class="flower-mark" role="img" aria-label="Lotus flower logo mark of Pertwick Candles"></div>
    <div class="divider"></div>
    <h1 class="brand-name">Pertwick Candles</h1>
    <p class="scent-name">Scent</p>
    <p class="product-type">SOJAKERZE</p>
    <p class="origin">Handgemacht in<br>der Schweiz</p>
  </main>
</body>
</html>
```